Plumber Referal Program for Water Damage Mitigation

A flyer describing incentives for plumbers to refer us as well as business information. We are called Vorl Restoration and we offer water damage mitigation, mold remediation, and sewage clean up as our 3 services. We are using blue as our company color, here are the following codes included in the logo.

Lighter blue, middle section of logo:
HEX: #2499c7
rgb(36,153,199)
hsl(197,69%,46%)

Darker blue, main color of logo and lettering:
HEX: #1a7da4
rgb(26,125,164)
hsl(197,73%,37%)

Lightest blue, only on small stars at top of logo:
HEX: #9bd3fc
rgb(155,211,252)
hsl(205,94%,80%)

Target Market(s)

Plumbers and other service industries.

Industry/Entity Type

Water Damage Restoration

Requirements
Must have
• Name of our company (Vorl Restoration) along with our number 1(800)555-0192. Website is vorlrestoration.example. 24/7 emergency response. Different methods of payment, including Payquill, Brindo, Coinlet Pay, and written checks. Please include 60-90 minute response time. Please include our 3 services, water damage mitigation, mold remediation, and sewage clean-up. A simple 2 sided flyer.
Nice to have
• Fairly simple design, not too busy. At least 1-2 pictures of water damage and/or mold remediation.
Should not have
• A dollar amount, we would like it to be open ended. Stock photos of smiling people.

```html
<!DOCTYPE html>
<html lang="en">
<head>
<meta charset="utf-8">
<title>Vorl Restoration – Plumber Referral Flyer</title>
<link href="https://fonts.googleapis.com/css2?family=Roboto:wght@400;700;900&family=Great+Vibes&display=swap" rel="stylesheet">
<style>
  :root{
    --blue-dark:#1a7da4;
    --blue-mid:#2499c7;
    --blue-light:#9bd3fc;
    --navy:#1f5e8c;
    --ink:#333;
    --grey:#6e6e6e;
    --white:#fff;
  }
  *{margin:0;padding:0;box-sizing:border-box}
  html,body{width:869px;height:1200px;overflow:hidden;background:var(--white)}
  body{font-family:"Roboto",Arial,sans-serif;color:var(--ink)}
  .flyer{position:relative;width:869px;height:1200px;overflow:hidden;background:var(--white)}

  .wall-photo{position:absolute;left:0;top:0;width:869px;height:600px;
    background:
      radial-gradient(ellipse 260px 200px at 640px 330px,rgba(236,228,214,.85),rgba(236,228,214,0) 70%),
      radial-gradient(ellipse 220px 160px at 760px 90px,rgba(230,220,204,.7),rgba(230,220,204,0) 70%),
      repeating-linear-gradient(90deg,rgba(120,84,40,.10) 0 6px,rgba(255,240,210,.06) 6px 34px),
      linear-gradient(135deg,#a77a44 0%,#c9a46f 35%,#d8bd93 60%,#cfae80 100%)}
  .hero-shapes{position:absolute;left:0;top:0}

  .pipe-photo{position:absolute;left:-90px;top:102px;width:550px;height:550px;border-radius:50%;
    background:
      radial-gradient(ellipse 120px 190px at 270px 330px,rgba(225,232,236,.55),rgba(225,232,236,0) 70%),
      radial-gradient(ellipse 170px 150px at 150px 270px,rgba(150,106,58,.95),rgba(150,106,58,0) 70%),
      radial-gradient(ellipse 120px 160px at 300px 170px,rgba(120,100,72,.7),rgba(120,100,72,0) 70%),
      radial-gradient(circle at 40% 50%,#3d3226 0%,#1b1713 55%,#0d0b09 100%);
    border:12px solid var(--navy);box-shadow:0 0 0 6px #e4e4e4,0 14px 24px rgba(0,0,0,.35)}

  .brand-badge{position:absolute;left:342px;top:486px;width:166px;height:166px;border-radius:50%;
    background:radial-gradient(circle at 40% 35%,#3aaedb 0%,var(--blue-mid) 60%,var(--blue-dark) 100%);
    box-shadow:0 6px 14px rgba(0,0,0,.25);
    display:flex;align-items:center;justify-content:center;text-align:center;
    color:var(--white);font-weight:900;font-size:21px;line-height:1.1;letter-spacing:.5px}

  .brand-dot{position:absolute;left:657px;top:40px;width:112px;height:112px;border-radius:50%;
    background:radial-gradient(circle at 40% 35%,var(--blue-mid),var(--blue-dark));
    box-shadow:0 0 12px rgba(255,255,255,.7)}
  .brand-name{position:absolute;left:580px;top:164px;font-weight:900;font-size:27px;color:var(--blue-dark);letter-spacing:-.2px;white-space:nowrap}

  .pitch{position:absolute;left:72px;top:702px;width:380px}
  .pitch-script{font-family:"Great Vibes",cursive;font-size:80px;color:var(--grey);line-height:1}
  .pitch-main{font-weight:700;font-size:61px;color:var(--blue-mid);line-height:1;margin-top:-12px;letter-spacing:.3px}
  .pitch-sub{font-size:37px;color:var(--grey);margin-top:4px;letter-spacing:.3px;line-height:1.05}
  .response{position:absolute;left:84px;top:915px;width:280px;text-align:center}
  .response-label{font-size:30px;color:#555;letter-spacing:.3px;line-height:1.1}
  .response-time{font-weight:700;font-size:35px;color:var(--navy);margin-top:2px;line-height:1.1}

  .service{position:absolute;left:478px;width:370px;padding-left:72px}
  .service svg{position:absolute;left:0}
  .service-water{top:667px}
  .service-mold{top:766px}
  .service-sewage{top:873px}
  .service-title{font-weight:700;font-size:16.5px;color:var(--navy);letter-spacing:.2px}
  .service-text{font-size:11.4px;color:#555;line-height:1.13;margin-top:5px;width:290px}

  .contact-bar{position:absolute;left:0;top:1019px;width:560px;height:80px;background:var(--navy)}
  .emergency-bar{position:absolute;left:530px;top:1008px;width:339px;height:97px;background:var(--blue-mid)}
  .contact-item{position:absolute;top:1050px;color:var(--white);font-size:15.5px;display:flex;align-items:center;gap:8px}
  .contact-web{left:26px}
  .contact-phone{left:308px}
  .emergency-seal{position:absolute;left:517px;top:1006px;width:96px;height:96px;border-radius:50%;
    background:var(--navy);border:2px solid var(--white);display:flex;align-items:center;justify-content:center}
  .emergency-text{position:absolute;left:620px;top:1024px;width:240px;text-align:center;color:var(--white)}
  .emergency-hours{font-size:38px;line-height:1}
  .emergency-label{font-size:17px;margin-top:4px;letter-spacing:.3px}

  .payments-label{position:absolute;left:15px;top:1108px;font-size:11px;color:#555}
  .payment{position:absolute;top:1131px;display:flex;align-items:center;gap:10px}
  .payment-a{left:24px}
  .payment-b{left:227px}
  .payment-c{left:418px}
  .payment-d{left:674px}
  .payment-square{width:44px;height:44px;background:#111;border-radius:4px}
  .payment-square.is-cheque{background:#333}
  .payment-name{font-weight:700;font-size:26px;color:#222}
</style>
</head>
<body>
<main class="flyer">
  <div class="wall-photo" role="img" aria-label="Photo of a cracked, water-stained beige wall"></div>

  <svg class="hero-shapes" width="869" height="640" viewBox="0 0 869 640" aria-hidden="true">
    <path d="M869,282 C820,290 780,320 784,385 C788,440 770,452 700,462 C640,472 600,500 586,537 C620,548 640,552 660,562 C690,575 740,585 780,592 L869,600 Z" fill="#fff"/>
    <path d="M869,288 C826,296 790,326 794,388 C798,444 778,458 706,468 C648,478 610,504 592,536 C630,546 648,552 668,562 C698,574 744,584 782,590 L869,598 Z" fill="var(--navy)"/>
    <path d="M500,600 C520,565 545,545 586,537 C620,548 650,556 680,568 C720,582 760,592 869,600 L869,640 L500,640 Z" fill="#fff"/>
  </svg>

  <div class="pipe-photo" role="img" aria-label="Close-up photo of water gushing from a rusty leaking pipe"></div>
  <div class="brand-badge">VORL<br>RESTORATION</div>

  <div class="brand-dot" aria-hidden="true"></div>
  <div class="brand-name">VORL RESTORATION</div>

  <section class="pitch">
    <div class="pitch-script">Get</div>
    <div class="pitch-main">REWARDED</div>
    <div class="pitch-sub">FOR REFERING US</div>
  </section>
  <section class="response">
    <div class="response-label">GET FEEDBACK IN</div>
    <div class="response-time">60-90 MINUTES</div>
  </section>

  <section class="service service-water">
    <svg style="top:-12px" width="46" height="52" viewBox="0 0 46 52" aria-hidden="true">
      <path d="M23,10 C30,22 37,30 37,38 A14,14 0 0 1 9,38 C9,30 16,22 23,10Z" fill="var(--navy)"/>
      <path d="M8,0 C12,7 15,10 15,14 A7,7 0 0 1 1,14 C1,10 4,7 8,0Z" fill="var(--navy)"/>
      <path d="M38,0 C42,7 45,10 45,14 A7,7 0 0 1 31,14 C31,10 34,7 38,0Z" fill="var(--navy)"/>
    </svg>
    <div class="service-title">WATER DAMAGE MITIGATION</div>
    <p class="service-text">Water damage mitigation involves prompt action to minimize the destructive effects of water intrusion, preserving property and preventing further harm.</p>
  </section>
  <section class="service service-mold">
    <svg style="top:-10px;left:-8px" width="56" height="56" viewBox="0 0 56 56" aria-hidden="true">
      <g stroke="var(--navy)" stroke-width="3" stroke-linecap="round">
        <line x1="28" y1="4" x2="28" y2="52"/><line x1="4" y1="28" x2="52" y2="28"/>
        <line x1="11" y1="11" x2="45" y2="45"/><line x1="45" y1="11" x2="11" y2="45"/>
      </g>
      <circle cx="28" cy="28" r="16" fill="var(--navy)"/>
      <circle cx="33" cy="24" r="4" fill="#fff"/><circle cx="24" cy="33" r="2.5" fill="#fff"/>
    </svg>
    <div class="service-title">MOLD REMEDIATION</div>
    <p class="service-text">Mold remediation is the process of safely and thoroughly removing mold growth from indoor environments to protect both human health and property integrity.</p>
  </section>
  <section class="service service-sewage">
    <svg style="top:-20px" width="50" height="52" viewBox="0 0 50 52" aria-hidden="true">
      <path d="M10,20 L40,20 L36,50 L14,50 Z" fill="var(--navy)"/>
      <path d="M12,20 C12,6 38,6 38,20" fill="none" stroke="var(--navy)" stroke-width="3"/>
    </svg>
    <div class="service-title">SEWAGE CLEAN-UP</div>
    <p class="service-text">Sewage clean-up is a critical and specialized task that involves the thorough removal and decontamination of hazardous waste materials from areas affected by sewage backups or spills, ensuring a safe and sanitary environment.</p>
  </section>

  <div class="contact-bar"></div>
  <div class="emergency-bar"></div>
  <div class="contact-item contact-web">
    <svg width="24" height="24" viewBox="0 0 24 24" aria-hidden="true" fill="none" stroke="#fff" stroke-width="1.6">
      <circle cx="12" cy="12" r="10"/><ellipse cx="12" cy="12" rx="4.5" ry="10"/><line x1="2" y1="12" x2="22" y2="12"/><line x1="4" y1="7" x2="20" y2="7"/><line x1="4" y1="17" x2="20" y2="17"/>
    </svg>
    <span>www.vorlrestoration.example</span>
  </div>
  <div class="contact-item contact-phone">
    <svg width="18" height="18" viewBox="0 0 24 24" aria-hidden="true"><path d="M6.6 10.8a15 15 0 0 0 6.6 6.6l2.2-2.2a1 1 0 0 1 1-.25 11.4 11.4 0 0 0 3.6.57 1 1 0 0 1 1 1V20a1 1 0 0 1-1 1A17 17 0 0 1 3 4a1 1 0 0 1 1-1h3.5a1 1 0 0 1 1 1c0 1.25.2 2.45.57 3.57a1 1 0 0 1-.25 1z" fill="#fff"/></svg>
    <span>1(800)555-0192</span>
  </div>
  <div class="emergency-seal">
    <svg width="62" height="62" viewBox="0 0 62 62" aria-hidden="true" fill="none" stroke="#fff" stroke-width="2.4" stroke-linejoin="round" stroke-linecap="round">
      <path d="M31,4 L45,9 L45,22 C45,31 38,36 31,39 C24,36 17,31 17,22 L17,9 Z" fill="#fff"/>
      <path d="M24,21 L29,26 L38,16" stroke="var(--navy)"/>
      <path d="M4,46 L14,44 L26,48 L36,48 M14,56 L36,57 L56,44 C54,41 50,41 48,43 L38,49"/>
    </svg>
  </div>
  <div class="emergency-text">
    <div class="emergency-hours">24/7</div>
    <div class="emergency-label">EMERGENCY RESPONSE</div>
  </div>

  <div class="payments-label">WE ACCEPT:</div>
  <div class="payment payment-a"><span class="payment-square"></span><span class="payment-name">Payquill</span></div>
  <div class="payment payment-b"><span class="payment-square"></span><span class="payment-name">Brindo</span></div>
  <div class="payment payment-c"><span class="payment-square"></span><span class="payment-name">Coinlet Pay</span></div>
  <div class="payment payment-d"><span class="payment-square is-cheque"></span><span class="payment-name">Checque</span></div>
</main>
</body>
</html>
```